PeakVoyageHub

1. Can you describe what your company does?

Please find enclosed documents for your reference about our business doing.

2. Who are your target customers for the website?

Company Positioning: A comprehensive supplier of premier international sports travel and high-end event services.
Core Advantage: Exclusive international partnership resources and an Official Ticketing Assurance System.
Service Standard: One-Stop, High-Quality Service Solutions based on the "An once-in-a-lifetime experience" philosophy.

Our target customers for the website:
Mid-to-High-end Sports Enthusiasts
Corporate Clients
Sports Associations
Please kindly find enclosed for more details about our target customers, I think it's very important to make it clear to you.

3. Do you have an existing domain name / website address?

Yes, I have. I just applied for this new domain and it's totally a new website. www.peakvoyagehub.example

4. In addition to a Home Page, which other pages / sections would you like your website to have:
About Us
Contact Us , Office / Mailing Address
Sports Travel Products( Bucket Lists) : Globe Shield, Crown Quartet, Panathlia, Football, CHL, Golf, Skiing, Hiking,Galas
Reviews/ Unforgettable Moments
FAQs
Any other page / section you would like: Here is the website for your reference, www.lanejaunts.example
For each of the pages / sections you’d like to have, please provide the text (and images, if available) you would like to include.
Please recommend 2-3 templates to me, and let me know what kind of text I will provide to every web pages.

5. Which of the below are features and functionalities your website will need:
Image Gallery
Videos
Contact Form
Maps
FAQs
6. Please provide the URLs for the social media profiles you'd like to link to the website.

Do you know Quiet Blue Ledger?

Please let me know anything you need, thank you very much!

Have a good day!

Target Market(s)

Travel for the world-wide sports games and make an once-in-a-lifetime experience

Industry/Entity Type

sports and travel industry

Coding

Coded - Design and coding required

Number of Pages Required

5+ page

Requirements
Must have
• our logo
Nice to have
• On the homepage, I’d like a banner-style section to prominently showcase the latest products.

```html
<!DOCTYPE html>
<html lang="en">
<head>
<meta charset="utf-8">
<title>PeakVoyageHub – Our Services</title>
<link rel="stylesheet" href="https://fonts.googleapis.com/css2?family=Catamaran:wght@300;400;500;700;800&family=Source+Sans+3:wght@400&display=swap">
<style>
  :root {
    --lime: #bcd85f;
    --lime-glow: rgba(188, 216, 95, 0.35);
    --ink: #121212;
    --nav: #141414;
    --card: #151515;
    --card-border: #262626;
    --white: #ffffff;
    --soft: #cfcfcf;
    --page: #ffffff;
    --caption: #1a1a1a;
  }
  * { margin: 0; padding: 0; box-sizing: border-box; }
  html, body { width: 1200px; height: 1200px; overflow: hidden; background: var(--page); }
  body { position: relative; font-family: "Catamaran", sans-serif; }

  .site { position: absolute; left: 32px; top: 155px; width: 1135px; height: 774px; background: var(--ink); overflow: hidden; }

  .topbar { height: 36px; background: var(--lime); display: flex; justify-content: flex-end; align-items: center; padding-right: 33px; gap: 7px; color: var(--white); font-size: 12.5px; font-weight: 400; }
  .topbar svg { width: 17px; height: 11px; }

  .navbar { height: 55px; background: var(--nav); border-bottom: 1px solid #222; position: relative; }
  .brand { position: absolute; left: 130px; top: 13px; font-size: 22px; font-weight: 800; color: var(--white); letter-spacing: 0.1px; }
  .menu { position: absolute; left: 407px; top: 17px; display: flex; gap: 23px; list-style: none; color: var(--white); font-size: 12.8px; font-weight: 500; }
  .menu li { display: flex; align-items: center; gap: 6px; }
  .menu svg { width: 12px; height: 11px; }

  .services-head { position: absolute; top: 204px; left: 0; width: 100%; text-align: center; }
  .services-title { color: var(--white); font-size: 31px; font-weight: 800; line-height: 1; }
  .services-rule { width: 60px; height: 2px; background: var(--lime); margin: 13px auto 0; }
  .services-lead { width: 500px; margin: 9px auto 0; color: var(--soft); font-size: 12.5px; font-weight: 300; line-height: 20px; }

  .cards { position: absolute; top: 334px; left: 131px; display: flex; gap: 24px; }
  .card { width: 275px; height: 342px; background: var(--card); border: 1px solid var(--card-border); border-radius: 8px; overflow: hidden; position: relative; }
  .card-photo { height: 152px; }
  .photo-track { background: linear-gradient(135deg, #a2453f 0%, #7d2d2a 45%, #3a2b2b 70%, #b0504a 100%); }
  .photo-meeting { background: linear-gradient(135deg, #3a3f46 0%, #6e5a48 40%, #c8873f 65%, #2a2d33 100%); }
  .photo-workout { background: linear-gradient(135deg, #f2f2ee 0%, #d9d3c4 45%, #e46a3c 60%, #8a6a4a 85%, #5a4331 100%); }
  .card-title { position: absolute; left: 18px; top: 175px; display: flex; align-items: center; gap: 12px; color: var(--white); font-size: 18.5px; font-weight: 700; }
  .card-title svg { width: 18px; height: 18px; }
  .card-text { position: absolute; left: 18px; top: 217px; width: 245px; color: #e4e4e4; font-size: 12.2px; font-weight: 400; line-height: 19.5px; }
  .card-button { position: absolute; left: 18px; top: 285px; width: 108px; height: 37px; border-radius: 19px; background: var(--lime); color: var(--white); font-size: 12.5px; font-weight: 500; display: flex; align-items: center; justify-content: center; box-shadow: 0 4px 14px var(--lime-glow); }

  .preview-note { position: absolute; left: 0; width: 1200px; text-align: center; font-family: "Source Sans 3", sans-serif; color: var(--caption); }
  .preview-lead { top: 992px; font-size: 24px; }
  .preview-link { top: 1052px; font-size: 24px; }
  .preview-body { top: 1112px; font-size: 17px; line-height: 22px; }
</style>
</head>
<body>
  <main class="site">
    <div class="topbar">
      <svg viewBox="0 0 17 11" aria-hidden="true"><path d="M1 0h15a1 1 0 0 1 1 1v3a1.5 1.5 0 0 0 0 3v3a1 1 0 0 1-1 1H1a1 1 0 0 1-1-1V7a1.5 1.5 0 0 0 0-3V1a1 1 0 0 1 1-1z" fill="#fff"/></svg>
      <span>Official Tickets to Top Global Events</span>
    </div>
    <nav class="navbar">
      <div class="brand">PeakVoyageHub</div>
      <ul class="menu">
        <li>Home</li><li>About</li><li>Services</li><li>Products</li><li>Gallery</li><li>FAQs</li><li>Contact</li>
        <li><svg viewBox="0 0 12 11" aria-hidden="true"><rect x="0.7" y="0.7" width="10.6" height="9.6" rx="1" fill="none" stroke="#fff" stroke-width="1.4"/><rect x="2.5" y="2.5" width="3" height="3" fill="#fff"/><path d="M7 3h3M7 5h3M2.5 7.5h7.5" stroke="#fff" stroke-width="1"/></svg>News</li>
      </ul>
    </nav>

    <header class="services-head">
      <h1 class="services-title">Our Services</h1>
      <div class="services-rule"></div>
      <p class="services-lead">Tailored experiences for different client segments with our exclusive partnerships and official ticketing system.</p>
    </header>

    <section class="cards">
      <article class="card">
        <div class="card-photo photo-track" role="img" aria-label="Sprinter crouched in starting blocks on a red running track"></div>
        <h2 class="card-title"><svg viewBox="0 0 18 18" aria-hidden="true"><circle cx="9" cy="5" r="4.3" fill="#bcd85f"/><path d="M1 18c0-5 3.5-7.5 8-7.5s8 2.5 8 7.5z" fill="#bcd85f"/></svg>Sports Enthusiasts</h2>
        <p class="card-text">For individuals seeking ultimate experiences with official, scarce seats for top-tier global events and personalized services.</p>
        <div class="card-button">Learn More</div>
      </article>
      <article class="card">
        <div class="card-photo photo-meeting" role="img" aria-label="Business team meeting around a conference table with laptops"></div>
        <h2 class="card-title"><svg viewBox="0 0 18 18" aria-hidden="true"><rect x="3" y="0" width="12" height="18" rx="1" fill="#bcd85f"/><g fill="#151515"><rect x="5" y="2.5" width="2" height="2"/><rect x="8" y="2.5" width="2" height="2"/><rect x="11" y="2.5" width="2" height="2"/><rect x="5" y="6" width="2" height="2"/><rect x="8" y="6" width="2" height="2"/><rect x="11" y="6" width="2" height="2"/><rect x="5" y="9.5" width="2" height="2"/><rect x="11" y="9.5" width="2" height="2"/><rect x="7.5" y="13" width="3" height="5"/></g></svg>Corporate Clients</h2>
        <p class="card-text">High-end incentive programs, conference services, and reliable event operations for businesses.</p>
        <div class="card-button">Learn More</div>
      </article>
      <article class="card">
        <div class="card-photo photo-workout" role="img" aria-label="Athlete doing sit-ups on a mat in a bright studio"></div>
        <h2 class="card-title"><svg viewBox="0 0 24 18" aria-hidden="true" style="width:23px"><circle cx="12" cy="5" r="3.6" fill="#bcd85f"/><circle cx="4.5" cy="4" r="2.6" fill="#bcd85f"/><circle cx="19.5" cy="4" r="2.6" fill="#bcd85f"/><path d="M5.5 17c0-4.5 3-6.5 6.5-6.5s6.5 2 6.5 6.5z" fill="#bcd85f"/><path d="M0 13c0-3 2-4.5 4.5-4.5 1.3 0 2.3.4 3 1-1.5 1-2.5 2.3-2.8 3.5z M24 13c0-3-2-4.5-4.5-4.5-1.3 0-2.3.4-3 1 1.5 1 2.5 2.3 2.8 3.5z" fill="#bcd85f"/></svg>Sports Associations</h2>
        <p class="card-text">Professional team travel, overseas competition support, and event operation services.</p>
        <div class="card-button">Learn More</div>
      </article>
    </section>
  </main>

  <p class="preview-note preview-lead">You can preview your website directly on Hostwell using this link:</p>
  <p class="preview-note preview-link">https://peakvoyagehub.hostwell.example/</p>
  <p class="preview-note preview-body">We take your security very seriously, and Hostwell is a trusted and reliable platform. Therefore, my team and I<br>have hosted the code so that you can explore and interact with your site with complete confidence.</p>
</body>
</html>
```